Design for large signage in retail outlet.

For a souvenir / gift shop, needing the design for a large sign for the hair braiding section of the shop. Needs to say
"Glimmerwave Cove Hair Braiding " plus pics / background
Bright, sparkly, colourful, eye catching, catering more for women and girls.
A combination of the file 1 and 2, I've supplied. File 3 is what I created, but did not like it. File 4 is typical off the braids we offer.

```html
<!DOCTYPE html>
<html lang="en">
<head>
<meta charset="utf-8">
<title>Glimmerwave Cove Hair Braiding</title>
<link rel="stylesheet" href="https://fonts.googleapis.com/css2?family=Montserrat:wght@900&family=Yellowtail&display=block">
<style>
  :root {
    --plum-deep: #1c0420;
    --plum-mid: #3a0538;
    --floor-glow: #7a1478;
    --gold-light: #fff3a8;
    --gold: #f6c431;
    --gold-dark: #b8860b;
    --silver-light: #ffffff;
    --silver: #c9ccd2;
    --silver-dark: #7d828c;
    --braid-top: #ff4b2b;
    --braid-bottom: #a98cf0;
    --script-pink: #f78bc0;
    --script-blue: #58a8f5;
  }
  html, body {
    margin: 0;
    padding: 0;
    width: 1200px;
    height: 341px;
    overflow: hidden;
    background: var(--plum-deep);
  }
  .sign {
    position: relative;
    width: 1200px;
    height: 341px;
    background:
      radial-gradient(ellipse 45% 55% at 42% 22%, var(--plum-mid) 0%, transparent 100%),
      linear-gradient(180deg, var(--plum-deep) 0%, #2a0530 55%, #45084a 70%, var(--floor-glow) 78%, #3a063c 100%);
  }
  .sign svg { display: block; }
  .script-word {
    font-family: "Yellowtail", "Brush Script MT", cursive;
  }
  .headline-word {
    font-family: "Montserrat", "Arial Black", sans-serif;
    font-weight: 900;
  }
  .headline-edge {
    fill: none;
    stroke: url(#goldEdge);
    stroke-width: 5;
    stroke-linejoin: round;
  }
  .headline-face {
    fill: url(#silverFill);
    stroke: none;
  }
</style>
</head>
<body>
<main class="sign">
  <svg width="1200" height="341" viewBox="0 0 1200 341" xmlns="http://www.w3.org/2000/svg">
    <defs>
      <linearGradient id="silverFill" x1="0" y1="0" x2="0" y2="1">
        <stop offset="0" stop-color="var(--silver-light)"/>
        <stop offset="0.45" stop-color="var(--silver)"/>
        <stop offset="1" stop-color="var(--silver-dark)"/>
      </linearGradient>
      <linearGradient id="goldEdge" x1="0" y1="0" x2="0" y2="1">
        <stop offset="0" stop-color="var(--gold-light)"/>
        <stop offset="1" stop-color="var(--gold-dark)"/>
      </linearGradient>
      <linearGradient id="scriptRainbow" x1="0" y1="0" x2="0" y2="1">
        <stop offset="0.15" stop-color="var(--gold)"/>
        <stop offset="0.6" stop-color="var(--script-pink)"/>
        <stop offset="1" stop-color="var(--script-blue)"/>
      </linearGradient>
      <linearGradient id="scriptGold" x1="0" y1="0" x2="0" y2="1">
        <stop offset="0" stop-color="var(--gold-light)"/>
        <stop offset="1" stop-color="var(--gold)"/>
      </linearGradient>
      <linearGradient id="crownFill" x1="0" y1="0" x2="0" y2="1">
        <stop offset="0" stop-color="#f3d25a"/>
        <stop offset="1" stop-color="#a87a12"/>
      </linearGradient>
      <linearGradient id="braidFill" x1="0" y1="0" x2="0" y2="1">
        <stop offset="0" stop-color="var(--braid-top)"/>
        <stop offset="0.6" stop-color="#f06a8a"/>
        <stop offset="1" stop-color="var(--braid-bottom)"/>
      </linearGradient>
      <linearGradient id="reflectionFade" x1="0" y1="0" x2="0" y2="1">
        <stop offset="0" stop-color="#fff" stop-opacity="0.4"/>
        <stop offset="1" stop-color="#fff" stop-opacity="0"/>
      </linearGradient>
      <mask id="reflectionMask">
        <rect x="0" y="247" width="1200" height="80" fill="url(#reflectionFade)"/>
      </mask>
      <g id="headlineSet">
        <text class="headline-word headline-edge" x="205" y="245" font-size="96" textLength="240" lengthAdjust="spacingAndGlyphs">HAIR</text>
        <text class="headline-word headline-edge" x="500" y="245" font-size="96" textLength="508" lengthAdjust="spacingAndGlyphs">BRAIDING</text>
        <text class="headline-word headline-face" x="205" y="245" font-size="96" textLength="240" lengthAdjust="spacingAndGlyphs">HAIR</text>
        <text class="headline-word headline-face" x="500" y="245" font-size="96" textLength="508" lengthAdjust="spacingAndGlyphs">BRAIDING</text>
      </g>
    </defs>

    <g class="headline-reflection" aria-hidden="true" mask="url(#reflectionMask)">
      <use href="#headlineSet" transform="translate(0 494) scale(1 -1)"/>
    </g>

    <g class="headline">
      <use href="#headlineSet"/>
    </g>

    <g class="crown-braids-illustration" role="img" aria-label="Gold jewelled crown resting on two long orange-to-lilac braids">
      <rect x="410" y="64" width="136" height="84" rx="10" fill="url(#crownFill)"/>
      <rect x="440" y="146" width="78" height="176" rx="26" fill="url(#braidFill)"/>
    </g>

    <g class="script-title">
      <text class="script-word" x="168" y="158" font-size="72" textLength="236" lengthAdjust="spacingAndGlyphs" fill="url(#scriptRainbow)" transform="rotate(-6 286 140)">Glimmerwave</text>
      <text class="script-word" x="548" y="118" font-size="84" fill="url(#scriptGold)" transform="rotate(-6 620 100)">Cove</text>
    </g>
  </svg>
</main>
</body>
</html>
```